Quorvix Letter head

Quorvix is a young and energetic software development consultancy. We spend our time working with clients to turn what ever is in their heads in to software.
We are trying to create an image of a high class software boutique who build class leading bespoke solutions.
We need a sharp letter head that looks great on high quality media.
We like bold colours and distinctive design. So show us what you can do.
Industry/Entity Type
Software
Requirements
Must have
- Our company is based in the UK and are requried to have on the paper somewhere the following information:
* Registered company name: Quorvix Ltd
* Registered company number
* VAT registration number
In addition we also want the following:
* An email address
* Telephone number
* Website address
An example of what some pages have in their footer is something like the following:
Quorvix Ltd is registered in England and Wales. Reg. no: 5316274
Registered office: 48 Cobblewick Road, Harlow Essex, CM93TP. Tel: 07712365081
You do not have to use this sentance but please make sure your design incorporates accommodates the requirements for UK based companies

```html
<!DOCTYPE html>
<html lang="en">
<head>
<meta charset="utf-8">
<title>Quorvix Letterhead</title>
<link href="https://fonts.googleapis.com/css2?family=Open+Sans:wght@300;400;600;700&display=swap" rel="stylesheet">
<style>
  :root {
    --brand-red: #c8283a;
    --paper: #ffffff;
    --text-grey: #7a7a7a;
    --logo-grey: #b4b4b4;
    --rule-grey: #bdbdbd;
  }
  * { margin: 0; padding: 0; box-sizing: border-box; }
  html, body { width: 848px; height: 1200px; overflow: hidden; background: var(--paper); }
  body { font-family: "Open Sans", Arial, sans-serif; color: var(--text-grey); }

  .letterhead {
    position: relative;
    width: 848px;
    height: 1200px;
    background: var(--paper);
    border: 8px solid var(--brand-red);
  }
  .letterhead__inner-frame {
    position: absolute;
    inset: 6px;
    border: 5px solid var(--brand-red);
  }

  .brand {
    position: absolute;
    left: 49px;
    top: 32px;
    display: flex;
    align-items: center;
    gap: 10px;
  }
  .brand__mark {
    width: 14px;
    height: 14px;
    background: var(--brand-red);
  }
  .brand__name {
    font-weight: 300;
    font-size: 44px;
    letter-spacing: 1px;
    line-height: 1;
    color: var(--logo-grey);
  }

  .contact {
    position: absolute;
    left: 606px;
    top: 18px;
    font-size: 10.5px;
    line-height: 14px;
    list-style: none;
  }
  .contact__item { display: flex; align-items: center; gap: 8px; height: 14px; }
  .contact__item--address { margin-bottom: 14px; }
  .contact__icon { width: 13px; height: 12px; flex: none; color: var(--text-grey); }
  .contact__at { width: 13px; text-align: center; font-size: 11px; flex: none; }

  .header-rule {
    position: absolute;
    left: 46px;
    top: 98px;
    width: 736px;
    height: 8px;
  }

  .footer-legal {
    position: absolute;
    left: 39px;
    top: 1118px;
    font-size: 11.5px;
    line-height: 16px;
  }
  .footer-legal__lead {
    font-weight: 700;
    font-size: 13.5px;
    margin-right: 20px;
  }
  .footer-legal__line--office { padding-left: 1px; }

  .footer-vat {
    position: absolute;
    left: 625px;
    top: 1117px;
    font-size: 14.5px;
  }
</style>
</head>
<body>
  <div class="letterhead">
    <div class="letterhead__inner-frame"></div>

    <header>
      <div class="brand">
        <span class="brand__mark"></span>
        <span class="brand__name">QUORVIX</span>
      </div>

      <ul class="contact">
        <li class="contact__item contact__item--address">
          <svg class="contact__icon" viewBox="0 0 13 12" aria-hidden="true">
            <path d="M1 6 L6.5 1 L12 6 M2.5 5 V11 H10.5 V5" fill="none" stroke="currentColor" stroke-width="1.2"/>
            <rect x="5" y="6.5" width="3" height="2" fill="currentColor"/>
          </svg>
          <span>your address here</span>
        </li>
        <li class="contact__item">
          <svg class="contact__icon" viewBox="0 0 13 12" aria-hidden="true">
            <path d="M1 4 Q6.5 0 12 4 L10.5 5.5 L8.5 4 L4.5 4 L2.5 5.5 Z" fill="currentColor"/>
            <rect x="3" y="6" width="7" height="5" rx="1" fill="none" stroke="currentColor" stroke-width="1.1"/>
          </svg>
          <span>Tel: 1234567889</span>
        </li>
        <li class="contact__item">
          <svg class="contact__icon" viewBox="0 0 13 12" aria-hidden="true">
            <rect x="3" y="1" width="7" height="4" fill="none" stroke="currentColor" stroke-width="1"/>
            <rect x="1" y="5" width="11" height="6" rx="1" fill="none" stroke="currentColor" stroke-width="1.1"/>
            <line x1="3" y1="8" x2="10" y2="8" stroke="currentColor" stroke-width="1"/>
          </svg>
          <span>Fax: 1223344566</span>
        </li>
        <li class="contact__item">
          <span class="contact__at">@</span>
          <span>Email: hello@quorvixmail.com</span>
        </li>
      </ul>

      <svg class="header-rule" viewBox="0 0 736 8" aria-hidden="true">
        <line x1="4" y1="4" x2="732" y2="4" stroke="var(--rule-grey)" stroke-width="1"/>
        <circle cx="4" cy="4" r="2.2" fill="var(--rule-grey)"/>
        <circle cx="732" cy="4" r="2.2" fill="var(--rule-grey)"/>
      </svg>
    </header>

    <footer>
      <div class="footer-legal">
        <p class="footer-legal__line"><span class="footer-legal__lead">Quorvix Ltd is</span>Quorvix Ltd is registered in England and Wales. Reg. no: 5316274</p>
        <p class="footer-legal__line">Directors Me and you, she and he</p>
        <p class="footer-legal__line footer-legal__line--office">Registered office: 48 Cobblewick Road, Harlow Essex, CM93TP. Tel: 07712365081</p>
      </div>
      <p class="footer-vat">VAT registration number</p>
    </footer>
  </div>
</body>
</html>
```